Clothing range for the petite modern mature woman needs a card design

We need a business card design for a new Sydney based company called river stone. We provide clothing to the modern mature woman who finds it difficult to source clothes that do not make them look frumpy or do not fit. We have an idea we would like an apple with the peel unravelling and possibly the silhouette of a woman's body coming out of the peel. The river stone represents the womans body shape and dressing it.

Target Market(s)

modern mature aged woman

Industry/Entity Type

Clothing

Contact Information for Business Card

abn: 42718063591
will provide email at a later date
a spiel re clothes for modern woman???

Font styles to use
Serif
Sans Serif

Requirements
Must have
• will need name - ABN -will need email address but still working on that (TBA)
Nice to have
• picture of an apple with its peel coming off and possibly the silhouette of a woman coming out. the issue a lot of women in the over 50 range have is that the clothing is very dated or makes the woman frumpy. we are providing clothes for the woman who has difficulty in finding fashionable clothes in their size.
Should not have
• don't want childlike

```html
<!DOCTYPE html>
<html lang="en">
<head>
<meta charset="utf-8">
<title>River Stone — Business Card</title>
<link rel="stylesheet" href="https://fonts.googleapis.com/css2?family=Jost:wght@400;500&display=swap">
<style>
  :root {
    --canvas-bg: #eef0ec;
    --lime: #c9d81c;
    --lime-soft: #d3df3a;
    --green: #14803c;
    --green-dark: #0e6a31;
    --paper: #ffffff;
    --shadow: rgba(20, 60, 30, 0.18);
  }
  * { box-sizing: border-box; margin: 0; padding: 0; }
  html, body {
    width: 1200px;
    height: 1000px;
    overflow: hidden;
    background: var(--canvas-bg);
    font-family: "Jost", "Futura", sans-serif;
  }
  .canvas {
    position: relative;
    width: 1200px;
    height: 1000px;
  }
  .card {
    position: absolute;
    top: 110px;
    width: 420px;
    height: 720px;
    box-shadow: 0 14px 34px var(--shadow);
  }
  .card--front {
    left: 150px;
    background: var(--lime);
  }
  .card--back {
    left: 630px;
    background: var(--paper);
  }

  /* Brand: plain mark above the name */
  .brand {
    position: absolute;
    left: 0;
    right: 0;
    display: flex;
    flex-direction: column;
    align-items: center;
    color: var(--green);
    font-weight: 400;
    letter-spacing: 0.02em;
  }
  .brand__mark {
    border-radius: 50%;
    background: var(--green);
    flex: none;
  }
  .card--front .brand {
    top: 90px;
    font-size: 50px;
  }
  .card--front .brand__mark {
    width: 300px;
    height: 300px;
    margin-bottom: 150px;
  }
  .card--back .brand {
    top: 60px;
    font-size: 42px;
  }
  .card--back .brand__mark {
    width: 120px;
    height: 120px;
    margin-bottom: 26px;
  }

  /* Contact bands */
  .bands {
    position: absolute;
    top: 300px;
    left: 0;
    right: 0;
    list-style: none;
  }
  .band {
    height: 46px;
    margin-bottom: 12px;
    background: var(--lime-soft);
    display: flex;
    align-items: center;
    justify-content: center;
    color: var(--green-dark);
    font-size: 22px;
    letter-spacing: 0.01em;
  }
  .band__label { font-weight: 500; }
  .band__sep { margin: 0 8px; font-weight: 400; }

  .details {
    position: absolute;
    top: 500px;
    left: 0;
    right: 0;
    text-align: center;
    color: var(--green-dark);
    font-size: 23px;
    font-weight: 500;
    line-height: 60px;
  }

  .lockup {
    position: absolute;
    right: 100px;
    bottom: 40px;
    display: flex;
    align-items: center;
    gap: 16px;
    color: var(--green);
    font-size: 30px;
    font-weight: 400;
  }
  .lockup .brand__mark {
    width: 60px;
    height: 60px;
    border-radius: 50%;
    background: var(--green);
  }
</style>
</head>
<body>
<main class="canvas">
  <section class="card card--front" aria-label="Card front">
    <div class="brand"><span class="brand__mark"></span><span class="brand__name">River Stone</span></div>
  </section>

  <section class="card card--back" aria-label="Card back">
    <div class="brand"><span class="brand__mark"></span><span class="brand__name">River Stone</span></div>
    <ul class="bands">
      <li class="band"><span class="band__label">Name Here</span><span class="band__sep">|</span><span>Position</span></li>
      <li class="band"><span class="band__label">t</span><span class="band__sep">|</span><span>01234567890</span></li>
      <li class="band"><span class="band__label">e</span><span class="band__sep">|</span><span>email@riverstone.com</span></li>
    </ul>
    <div class="details">
      <p class="details__web">www.riverstone.com</p>
      <p class="details__abn">abn: 42718063591</p>
    </div>
  </section>

  <div class="lockup"><span class="brand__mark"></span><span>River Stone</span></div>
</main>
</body>
</html>
```